PLIMOR

Require a design to fit on an A5 page, this is a page within a booklet by others hence it needs to be portable to that end user.
I have attached a picture of a banner we have used in the past as a basis for the design.
As this is for a conference on vegetable growing it needs to have that theme within the design together with the attached logo and a web/ email address and phone number.
Our products dispense fertiliser into irrigation water which is termed fertigation
www.quorvitdosingunits.com.au for further reference.

Reason: some designers that indicated they had accepted the project late need some more time

```html
<!DOCTYPE html>
<html lang="en">
<head>
<meta charset="utf-8">
<title>PLIMOR – Fertigation Page</title>
<link rel="stylesheet" href="https://fonts.googleapis.com/css2?family=Oswald:wght@500&family=Playfair+Display:wght@400;700&family=Fira+Sans:ital,wght@1,800&display=swap">
<style>
  :root {
    --backdrop: #f4f4f4;
    --olive: #a39448;
    --ink: #231f20;
    --leaf: #1e5a2b;
    --sun: #f3e51b;
    --paper: #ffffff;
    --shade: rgba(20, 14, 6, 0.32);
  }
  * { margin: 0; padding: 0; box-sizing: border-box; }
  html, body {
    width: 1200px;
    height: 1021px;
    overflow: hidden;
    background: var(--backdrop);
  }
  .page {
    position: absolute;
    left: 283px;
    top: 60px;
    width: 633px;
    height: 900px;
    background: var(--olive);
    overflow: hidden;
  }
  .display-type {
    position: absolute;
    inset: 0;
    width: 633px;
    height: 900px;
  }
  .display-type text {
    font-family: "Oswald", "Arial Narrow", sans-serif;
    font-weight: 500;
    fill: var(--ink);
  }
  .shadow-block {
    position: absolute;
    left: 66px;
    top: 337px;
    width: 252px;
    height: 282px;
    background: var(--shade);
  }
  .produce-collage {
    position: absolute;
    left: 2px;
    top: 291px;
    width: 284px;
    height: 279px;
    border: 3px solid var(--paper);
    background: linear-gradient(135deg, #5f7a2c 0%, #c08a4a 30%, #d8cfae 50%, #c2301e 72%, #8a9a3a 100%);
  }
  .bloom-mark {
    position: absolute;
    left: 453px;
    top: 250px;
    width: 290px;
    height: 290px;
    border-radius: 50%;
    background: var(--paper);
  }
  .bloom-mark .core {
    position: absolute;
    left: 117px;
    top: 117px;
    width: 56px;
    height: 56px;
    border-radius: 50%;
    background: var(--ink);
  }
  .tagline {
    position: absolute;
    left: 0;
    top: 605px;
    width: 226px;
    text-align: center;
    line-height: 1;
  }
  .tagline span { display: block; }
  .tagline .change {
    font-family: "Fira Sans", "Arial", sans-serif;
    font-style: italic;
    font-weight: 800;
    color: var(--leaf);
    font-size: 27px;
    letter-spacing: 4px;
  }
  .tagline .the-way {
    font-family: "Fira Sans", "Arial", sans-serif;
    font-style: italic;
    font-weight: 800;
    color: var(--leaf);
    font-size: 28px;
    letter-spacing: 4px;
    margin-top: 13px;
  }
  .tagline .you {
    font-family: "Playfair Display", Georgia, serif;
    font-weight: 400;
    color: var(--sun);
    font-size: 50px;
    margin-top: 14px;
  }
  .tagline .think,
  .tagline .about {
    font-family: "Playfair Display", Georgia, serif;
    font-weight: 400;
    color: var(--ink);
    font-size: 30px;
    letter-spacing: 6px;
  }
  .tagline .think { margin-top: 10px; }
  .tagline .about { margin-top: 10px; }
  .tagline .fertilizing {
    font-family: "Playfair Display", Georgia, serif;
    font-weight: 700;
    color: var(--paper);
    font-size: 31px;
    letter-spacing: 1px;
    margin-top: 10px;
  }
</style>
</head>
<body>
  <main class="page">
    <svg class="display-type" viewBox="0 0 633 900" aria-label="QUORVIT">
      <text x="-30" y="279" font-size="560" letter-spacing="-12">QU</text>
      <text x="225" y="905" font-size="440" letter-spacing="-6">ORV</text>
    </svg>

    <div class="bloom-mark" role="img" aria-label="White flower-shaped graphic"><div class="core"></div></div>

    <div class="shadow-block"></div>
    <div class="produce-collage" role="img" aria-label="Collage of fresh vegetables: beans, potatoes, broccoli, tomatoes, fennel, mushrooms, chillies, lettuce and radicchio"></div>

    <h1 class="tagline">
      <span class="change">CHANGE</span>
      <span class="the-way">the way</span>
      <span class="you">YOU</span>
      <span class="think">think</span>
      <span class="about">about</span>
      <span class="fertilizing">Fertilizing</span>
    </h1>
  </main>
</body>
</html>
```